Eye catching Bottle label for pink gin targeting women 25+

We need a new label for a re-launch of our shimmering strawberry pink gin liqueur. We would like it to look premium and eye catching on the shelf. We have 2 labels we require, one for 200ml bottle (2x2 inches) and one for 500ml bottle 4x4 inches). Label must state the ml of the bottle abd that it is 18.75%Vol. Also say Shimmering Strawberry Gin Liqueur with the brand name at the top - Harlow Vale Distillers. We have a logo but it doesn't need to be used if it doesn't work with the design/colours. The gin is presented in a clear bottle and is pink and sparkly. See uploaded image for reference.

Target Market(s)

Women aged 25-45

Font styles to use
Decorative

Colors
f59296
fbd4d5
eea4c8

Requirements
Must have
• Bottle size - 500ml/200ml
• Must say 18.75% Vol
• Must have brand name - Harlow Vale Distillers
• Must have product name - Glittering Blush Raspberry
• Must say - Gin Liqueur
Nice to have
• Some sort of floral or swirley background detail would be nice
Should not have
• Must not appeal to children

```html
<!DOCTYPE html>
<html lang="en">
<head>
<meta charset="utf-8">
<title>Harlow Vale Distillers – Glittering Blush Raspberry Gin Liqueur Label</title>
<link href="https://fonts.googleapis.com/css2?family=Poppins:wght@600;700;800&display=swap" rel="stylesheet">
<style>
  :root {
    --canvas-bg: #e2e2e2;
    --label-blush: #ecc8c9;
    --pattern-tone: #f0d3d2;
    --gin-magenta: #de2f7e;
    --band-pink: #de7fb5;
    --footer-pink: #efcfd1;
    --cocoa: #6b3530;
    --cream: #f6e9e3;
    --white: #ffffff;
  }
  * { box-sizing: border-box; margin: 0; padding: 0; }
  html, body {
    width: 867px;
    height: 1200px;
    overflow: hidden;
    background: var(--canvas-bg);
    font-family: "Poppins", sans-serif;
  }
  .canvas {
    position: relative;
    width: 867px;
    height: 1200px;
  }
  .label {
    position: absolute;
    left: 33px;
    top: 207px;
    width: 800px;
    height: 785px;
    background: var(--label-blush);
    overflow: hidden;
  }
  .label__pattern {
    position: absolute;
    inset: 0;
    background: radial-gradient(circle at 50% 40%, var(--pattern-tone) 0%, var(--label-blush) 75%);
  }
  .brand-seal {
    position: absolute;
    left: 322px;
    top: 16px;
    width: 182px;
    height: 182px;
    border-radius: 50%;
    background: var(--cocoa);
    display: flex;
    align-items: center;
    justify-content: center;
    text-align: center;
  }
  .brand-seal__name {
    color: var(--cream);
    font-weight: 600;
    font-size: 25px;
    line-height: 1.2;
  }
  .product-type {
    position: absolute;
    left: 0;
    width: 100%;
    text-align: center;
    color: var(--gin-magenta);
    font-weight: 700;
  }
  .product-type--gin {
    top: 248px;
    font-size: 218px;
    line-height: 1;
    letter-spacing: -4px;
  }
  .product-type--liqueur {
    top: 462px;
    font-size: 64px;
    line-height: 1;
    letter-spacing: 1px;
  }
  .flavour-band {
    position: absolute;
    left: 0;
    top: 562px;
    width: 100%;
    height: 140px;
    background: var(--band-pink);
    display: flex;
    flex-direction: column;
    align-items: center;
    justify-content: center;
    color: var(--white);
    font-weight: 700;
    font-size: 54px;
    line-height: 1.08;
    text-align: center;
  }
  .details-strip {
    position: absolute;
    left: 0;
    top: 702px;
    width: 100%;
    height: 83px;
    background: var(--footer-pink);
    display: flex;
    align-items: center;
    justify-content: center;
    color: var(--cocoa);
    font-weight: 700;
    font-size: 36px;
  }
</style>
</head>
<body>
  <main class="canvas">
    <section class="label">
      <div class="label__pattern" role="img" aria-label="Soft floral swirl background pattern in pale blush tones"></div>
      <div class="brand-seal">
        <span class="brand-seal__name">Harlow Vale<br>Distillers</span>
      </div>
      <h1 class="product-type product-type--gin">GIN</h1>
      <p class="product-type product-type--liqueur">LIQUEUR</p>
      <div class="flavour-band">
        <span>GLITTERING</span>
        <span>BLUSH RASPBERRY</span>
      </div>
      <div class="details-strip">500ml |18.75% Vol</div>
    </section>
  </main>
</body>
</html>
```